WEBSITE: Security Officer Training, Security Officer Certifications, Security Officer Job Training

colorful and simple website, NO FLASH, and easy for SEO
Able to Upload to GODADDY WEBSITE BUILDER!

We need a great image that depicts and sell Watchpost Learning Hub
Our websites for info: Security Officers doing cool things, the pictures must be great..

FEEL Free to choose ideas from our services in our
Www.watchpostlearninghub.org site
The CPO certified protection officer tab
The CFO certified Firearms Office tab
The Security Officer Academy
The Campus security officer
Will be a few pages, landing page and contact page..
Www.watchpostlearninghub.org
Www.civicwardcollege.net
Www.beaconcredentialsdesk.com
ALSO go to goggle and put in
Los Angles "Security Guard Training"
California Guard Card
Guard Card
Firearms Training
And similar words to see competitors websites!

WE want our more KICK ASS and COOOL!

OUr Industry: Security Officer Training Certifications
INFO: SECURITY OFFICER TRAINING
Law Enforcement
Police
Criminal Justice Training
Security Guards
Security Professional

Target Market(s)

Law Enforcement Training
Police Training
Criminal Justice Training
Security Officer Training
Security Officer Certifications

Industry/Entity Type

Security

Number of Pages Required

3 page

Requirements
Must have
• Able to upload to GODADDY WEBSITE BUILDER
• Easy to edit
• Must be easy for SEO
• NO FLASH or other things that prevent mobile phones
• MOBILE PHONE COMPATIBLE
• COOL!
• Call to action
• Contact form for email sign ups
• PICTURES SLIDE SHOW MUST HAVE
Should not have
• NO have flash

```html
<!DOCTYPE html>
<html lang="en">
<head>
<meta charset="utf-8">
<title>Watchpost Learning Hub — Security Guard Training</title>
<link href="https://fonts.googleapis.com/css2?family=Lato:wght@300;400;700;900&display=swap" rel="stylesheet">
<style>
:root{
  --gold:#f0c33c;
  --gold-soft:#f3d677;
  --gold-deep:#d9a81f;
  --ink:#1c1c1c;
  --dark:#222325;
  --panel:#3a3b3d;
  --grey:#f2f2f2;
  --line:#c9c9c9;
  --text:#444;
  --muted:#888;
  --fb:#3b5998;
  --tw:#8ec3e0;
  --white:#fff;
}
*{box-sizing:border-box;margin:0;padding:0}
html,body{width:1200px;height:3214px;overflow:hidden}
body{font-family:'Lato',sans-serif;color:var(--text);background:var(--white);position:relative}

/* header */
.site-header{position:absolute;left:0;top:0;width:1200px;height:138px;background:var(--white)}
.top-links{position:absolute;right:0;top:0;width:330px;height:34px;background:var(--ink);clip-path:polygon(8% 0,100% 0,100% 100%,0 100%);display:flex;align-items:center;justify-content:flex-end;gap:28px;padding-right:70px;color:var(--white);font-size:13px;font-weight:700;letter-spacing:.5px}
.contact-line{position:absolute;left:728px;font-size:16px;font-weight:700;color:var(--ink);display:flex;align-items:center;gap:10px}
.nav-bar{position:absolute;left:0;top:86px;width:1200px;height:52px;background:var(--gold);display:flex;align-items:center}
.nav-bar ul{list-style:none;display:flex;margin-left:257px;height:52px}
.nav-bar li{height:52px;display:flex;align-items:center;padding:0 28px;font-size:14px;font-weight:700;color:var(--ink);letter-spacing:.3px;border-right:1px solid rgba(0,0,0,.15)}
.nav-bar li.active{background:var(--ink);color:var(--gold);padding:0 27px}
.nav-bar li:last-child{border-right:0}
.brand{position:absolute;left:96px;top:8px;width:140px;height:200px;display:flex;flex-direction:column;align-items:center;z-index:3}
.brand-mark{width:124px;height:124px;border-radius:50%;background:var(--gold-deep);border:5px solid var(--white);box-shadow:0 2px 6px rgba(0,0,0,.25)}
.brand-name{margin-top:6px;font-size:14px;font-weight:900;color:var(--ink);text-align:center;line-height:1.1;background:var(--white);padding:3px 6px}

/* hero */
.hero{position:absolute;left:0;top:138px;width:1200px;height:516px;background:linear-gradient(120deg,#5d5248 0%,#8b7c6d 35%,#b9ad9c 60%,#4a4f5c 100%)}
.hero-caption{position:absolute;left:0;top:322px;width:620px;height:102px;background:rgba(20,20,20,.55);padding:12px 0 0 100px;color:var(--gold);font-size:28px;font-weight:700;line-height:1.3}

/* about */
.about{position:absolute;left:0;top:654px;width:1200px;height:561px;background:radial-gradient(ellipse at 50% 100%,#e4e4e4 0%,#f6f6f6 60%,#fff 100%);overflow:hidden}
.section-title{font-size:34px;font-weight:400;color:var(--ink);text-align:center}
.section-title span{color:var(--gold)}
.title-rule{position:relative;width:420px;height:20px;margin:8px auto 0}
.title-rule:before{content:"";position:absolute;left:0;right:0;top:9px;border-top:1px solid var(--line)}
.title-rule i{position:absolute;left:202px;top:0;width:16px;height:20px;border-radius:50%;background:var(--muted)}
.about-text{width:1040px;margin:20px auto 0;font-size:13px;line-height:1.6;text-align:center;color:#555}
.arc{position:absolute;left:343px;top:303px;width:514px;height:514px;border-radius:50%;background:radial-gradient(circle,#f8f8f8 0%,#dadada 70%,#cfcfcf 100%);border:2px solid #e6e6e6}
.hub{position:absolute;left:540px;top:405px;width:120px;height:120px;border-radius:50%;background:var(--gold-deep);border:5px solid var(--white);display:flex;align-items:center;justify-content:center;text-align:center;font-size:13px;font-weight:900;color:var(--white);line-height:1.1}
.feature{position:absolute;width:78px;height:78px;border-radius:50%;background:var(--white);border:5px solid #e1e1e1;display:flex;align-items:center;justify-content:center;box-shadow:0 1px 4px rgba(0,0,0,.15)}
.feature svg{width:40px;height:40px}
.feature-label{position:absolute;font-size:14px;font-weight:700;color:var(--ink);letter-spacing:.3px}

/* training */
.training{position:absolute;left:0;top:1215px;width:1200px;height:467px;background:linear-gradient(180deg,#3b3c3f,#2a2b2e 60%,#3a3834)}
.training .section-title{color:var(--white);padding-top:44px}
.course{position:absolute;width:488px;height:123px;background:rgba(110,110,112,.75);padding:22px 28px;color:var(--white)}
.course h3{font-size:22px;font-weight:700;margin-bottom:10px}
.course p{font-size:13px;line-height:1.55;color:#eee}
.course .plus{position:absolute;right:0;bottom:0;width:16px;height:16px;background:var(--white);color:var(--ink);font-size:14px;font-weight:900;line-height:15px;text-align:center}

/* experience / videos */
.col-title{position:absolute;font-size:31px;color:var(--ink);font-weight:400}
.col-title span{color:var(--gold)}
.col-rule{position:absolute;height:20px}
.col-rule:before{content:"";position:absolute;left:36px;right:0;top:9px;border-top:1px solid var(--line)}
.col-rule i{position:absolute;left:0;top:0;width:16px;height:20px;border-radius:50%;background:var(--muted)}
.exp-list{position:absolute;left:99px;top:1804px;list-style:none}
.exp-list li{display:flex;align-items:center;gap:12px;height:41.6px;font-size:13.5px;font-weight:700;color:var(--ink)}
.video{position:absolute;left:628px;top:1817px;width:473px;height:309px;background:linear-gradient(135deg,#2b2b2b,#4a4a4a 55%,#1d1d1d)}
.video-title{position:absolute;left:46px;top:100px;color:var(--white);font-size:25px;font-weight:700;line-height:1.1}
.play{position:absolute;left:200px;top:118px;width:72px;height:50px;border-radius:12px;background:#cc1f1f}
.video-bar{position:absolute;left:0;bottom:0;width:473px;height:34px;background:rgba(0,0,0,.75)}

/* inquiry */
.inquiry{position:absolute;left:0;top:2169px;width:1200px;height:328px;background:linear-gradient(90deg,#e9c36a,#f2d58d 50%,#e5bd5e)}
.inquiry-pill{position:absolute;left:118px;top:2272px;width:720px;height:139px;border-radius:70px 0 0 70px;background:rgba(255,255,255,.35);padding:18px 34px}
.inquiry-pill .inner{background:var(--gold);height:103px;border-radius:8px;padding:10px 36px;color:var(--white)}
.inquiry-pill b{display:block;font-size:44px;font-weight:700;line-height:1.1}
.inquiry-pill span{font-size:36px;font-weight:400}
.inquiry-photo{position:absolute;left:790px;top:2224px;width:230px;height:230px;border-radius:50%;background:radial-gradient(circle at 60% 40%,#d8d8d8,#8a8a8a);border:10px solid rgba(255,255,255,.6)}

/* social */
.social{position:absolute;left:0;top:2497px;width:1200px;height:375px;background:var(--grey)}
.feed{position:absolute;top:2540px;width:262px;height:293px;background:var(--white)}
.feed-head{height:34px;display:flex;align-items:center;justify-content:space-between;padding:0 12px;color:var(--white);font-size:12px}
.feed-head b{font-size:13px;font-weight:900}
.feed-item{display:flex;gap:10px;padding:12px 12px 4px}
.thumb{width:50px;height:42px;flex:none;background:linear-gradient(135deg,#8b6a46,#3d3025)}
.avatar{width:40px;height:40px;flex:none;border-radius:2px;background:#b9b9b9}
.feed-item p{font-size:11px;line-height:1.4}
.feed-item small{display:block;font-size:9.5px;color:var(--muted)}
.feed-foot{position:absolute;left:0;bottom:0;width:100%;padding:8px 12px;font-size:10px;color:var(--muted);border-top:1px solid #ddd}
.newsletter{position:absolute;left:692px;top:2540px;width:409px;height:293px;background:var(--white);border:6px solid #e2e2e2;text-align:center;padding:18px 28px}
.newsletter h4{font-size:22px;font-weight:400;color:var(--ink)}
.newsletter h4 span{color:var(--gold)}
.newsletter p{font-size:12.5px;line-height:1.6;margin-top:18px;color:#555}
.newsletter small{display:block;font-size:10px;color:var(--muted);margin-top:2px}
.field{height:30px;border:1px solid #e3e3e3;margin-top:8px;display:flex;align-items:center;gap:10px;padding-left:10px;font-size:11px;color:#aaa;text-align:left}
.btn{display:inline-block;background:var(--gold);color:var(--ink);font-weight:700;font-size:14px;padding:8px 18px;border-radius:3px}

/* footer */
.site-footer{position:absolute;left:0;top:2872px;width:1200px;height:295px;background:var(--dark);color:#ddd}
.foot-title{position:absolute;top:44px;font-size:16px;font-weight:700;color:var(--white)}
.foot-title span{color:var(--gold)}
.foot-links{position:absolute;left:99px;top:80px;list-style:none}
.foot-links li{font-size:12px;height:33px;display:flex;align-items:center;gap:12px}
.foot-links li:before{content:"";width:6px;height:6px;background:var(--gold)}
.foot-input{position:absolute;left:333px;width:256px;height:34px;background:var(--white);border-radius:3px;font-size:11px;color:#999;padding:10px 10px}
.foot-info{position:absolute;left:690px;top:80px;font-size:12px;line-height:1.45}
.foot-info b{color:var(--white);font-size:13px}
.foot-info .row{display:flex;align-items:center;gap:10px;height:33px}
.foot-seal{position:absolute;left:988px;top:70px;width:112px;height:160px;border-radius:50%;border:3px solid #777;background:#3a3a3a}
.bottom-bar{position:absolute;left:0;top:3167px;width:1200px;height:47px;background:var(--gold)}
.bottom-bar p{position:absolute;left:99px;top:16px;font-size:12px;font-weight:700;color:var(--ink)}
.follow{position:absolute;right:0;top:0;width:450px;height:47px;background:var(--ink);clip-path:polygon(8% 0,100% 0,100% 100%,0 100%);display:flex;align-items:center;gap:10px;padding-left:74px;color:var(--white);font-size:18px;font-weight:700}
.follow i{width:32px;height:32px;border-radius:50%;border:2px solid #ccc}
</style>
</head>
<body>

<header class="site-header">
  <div class="top-links"><span>FAQ'S</span><span>CONTACT US</span></div>
  <div class="contact-line" style="top:8px">
    <svg width="18" height="18" viewBox="0 0 24 24"><circle cx="12" cy="12" r="12" fill="var(--gold)"/><path d="M8 6l3 3-2 2c1 2 2 3 4 4l2-2 3 3-2 2c-5 0-10-5-10-10z" fill="#fff"/></svg>
    (555) 014-2290
  </div>
  <div class="contact-line" style="top:50px">
    <svg width="16" height="20" viewBox="0 0 16 20"><path d="M8 0a7 7 0 0 0-7 7c0 5 7 13 7 13s7-8 7-13a7 7 0 0 0-7-7z" fill="var(--gold)"/><circle cx="8" cy="7" r="2.5" fill="#fff"/></svg>
    1200 Harbor Gate Ave Fairview, CA 90000
  </div>
  <nav class="nav-bar">
    <ul>
      <li class="active">HOME</li>
      <li>ABOUT US</li>
      <li>OUR SERVICES</li>
      <li>GUARDCARDDESK</li>
      <li>SECURITY JOBS</li>
    </ul>
  </nav>
  <div class="brand">
    <div class="brand-mark"></div>
    <div class="brand-name">Watchpost<br>Learning Hub</div>
  </div>
</header>

<section class="hero" role="img" aria-label="Photo of a class of security guard trainees practising firearm drills in a classroom">
  <div class="hero-caption">Security Guard Training In Los Angeles<br>California Guard Card Specialists</div>
</section>

<section class="about">
  <h2 class="section-title" style="padding-top:42px">ABOUT <span>US</span></h2>
  <div class="title-rule"><i></i></div>
  <p class="about-text">Lorem ipsum dolor sit amet, consectetuer adipiscing elit, sed diam nonummy nibh euismod tincidunt ut laoreet dolore magna aliquam erat volutpat. Ut wisi enim ad minim veniam, quis nostrud exerci tation ullamcorper suscipit lobortis nisl ut aliquip ex ea commodo consequat. Duis autem vel eum iriure dolor in hendrerit in vulputate velit esse molestie consequat, vel illum dolore eu feugiat nulla facilisis at vero eros et accumsan et iusto odio dignissim.</p>
  <div class="arc"></div>
  <div class="hub">Watchpost<br>Learning<br>Hub</div>

  <div class="feature" style="left:454px;top:224px"><svg viewBox="0 0 40 40"><path d="M20 34L6 20a8 8 0 0 1 14-10 8 8 0 0 1 14 10z" fill="#333"/></svg></div>
  <div class="feature-label" style="left:360px;top:254px">VALUABLE!</div>
  <div class="feature" style="left:664px;top:224px"><svg viewBox="0 0 40 40"><circle cx="20" cy="22" r="13" fill="none" stroke="#333" stroke-width="3"/><path d="M20 22V14M16 5h8" stroke="#333" stroke-width="3"/></svg></div>
  <div class="feature-label" style="left:760px;top:254px">FAST</div>
  <div class="feature" style="left:325px;top:325px"><svg viewBox="0 0 40 40"><ellipse cx="15" cy="28" rx="9" ry="4" fill="#333"/><ellipse cx="15" cy="22" rx="9" ry="4" fill="#333"/><ellipse cx="15" cy="16" rx="9" ry="4" fill="#333"/><circle cx="29" cy="26" r="8" fill="#333"/></svg></div>
  <div class="feature-label" style="left:208px;top:355px">AFFORDABLE!</div>
  <div class="feature" style="left:792px;top:325px"><svg viewBox="0 0 40 40"><rect x="4" y="8" width="24" height="18" fill="none" stroke="#333" stroke-width="3"/><circle cx="27" cy="26" r="6" fill="none" stroke="#333" stroke-width="3"/><path d="M31 30l6 6" stroke="#333" stroke-width="3"/></svg></div>
  <div class="feature-label" style="left:886px;top:355px">JOB PLACEMENT</div>
  <div class="feature" style="left:255px;top:460px"><svg viewBox="0 0 40 40"><rect x="5" y="8" width="30" height="27" fill="none" stroke="#333" stroke-width="3"/><path d="M5 15h30M12 4v8M28 4v8" stroke="#333" stroke-width="3"/><path d="M11 21h4M18 21h4M25 21h4M11 28h4M18 28h4M25 28h4" stroke="#333" stroke-width="3"/></svg></div>
  <div class="feature-label" style="left:142px;top:490px">CONVENIENT!</div>
  <div class="feature" style="left:872px;top:460px"><svg viewBox="0 0 40 40"><rect x="4" y="12" width="20" height="22" fill="#333"/><circle cx="27" cy="22" r="10" fill="#333"/><path d="M22 22l4 4 6-7" fill="none" stroke="#fff" stroke-width="3"/></svg></div>
  <div class="feature-label" style="left:960px;top:490px">COMPLIANCE</div>
</section>

<section class="training" role="img" aria-label="Blurred photo of uniformed security officers in the background">
  <h2 class="section-title">Training <span>&amp; Certifications</span></h2>
</section>
<article class="course" style="left:99px;top:1363px"><h3>CPO certified protection officer</h3><p>TheCertified Protection Officer (CPO)program is designed to get your security guard training in Los Angeles.</p><span class="plus">+</span></article>
<article class="course" style="left:613px;top:1363px"><h3>CFO certified Firearms Office</h3><p>TheSecurity Officer Academy (SOA Cadet) program is designed for beginer and advanced security officers.</p><span class="plus">+</span></article>
<article class="course" style="left:99px;top:1516px"><h3>Security Officer Academy</h3><p>The Certified Firearms Officer (CFO) program is designed for Advanced employment in the security field.</p><span class="plus">+</span></article>
<article class="course" style="left:613px;top:1516px"><h3>CPO certified protection officer</h3><p>TheCampus Security Officer (CSO)program is designed for officers entry into working with school districts K-12.</p><span class="plus">+</span></article>

<h2 class="col-title" style="left:99px;top:1716px">Our <span>Experience</span></h2>
<div class="col-rule" style="left:99px;top:1772px;width:475px"><i></i></div>
<ul class="exp-list">
  <li><svg width="16" height="16" viewBox="0 0 16 16"><rect x="1" y="3" width="12" height="12" fill="none" stroke="#333" stroke-width="1.5"/><path d="M4 8l3 3 8-10" fill="none" stroke="#333" stroke-width="2.5"/></svg>United States Marine Corps</li>
  <li><svg width="16" height="16" viewBox="0 0 16 16"><rect x="1" y="3" width="12" height="12" fill="none" stroke="#333" stroke-width="1.5"/><path d="M4 8l3 3 8-10" fill="none" stroke="#333" stroke-width="2.5"/></svg>Advanced Patrol Officer</li>
  <li><svg width="16" height="16" viewBox="0 0 16 16"><rect x="1" y="3" width="12" height="12" fill="none" stroke="#333" stroke-width="1.5"/><path d="M4 8l3 3 8-10" fill="none" stroke="#333" stroke-width="2.5"/></svg>California Licensed Instructor: TIB 0000</li>
  <li><svg width="16" height="16" viewBox="0 0 16 16"><rect x="1" y="3" width="12" height="12" fill="none" stroke="#333" stroke-width="1.5"/><path d="M4 8l3 3 8-10" fill="none" stroke="#333" stroke-width="2.5"/></svg>Staff Sergeant-Infantry-Embassy Duty</li>
  <li><svg width="16" height="16" viewBox="0 0 16 16"><rect x="1" y="3" width="12" height="12" fill="none" stroke="#333" stroke-width="1.5"/><path d="M4 8l3 3 8-10" fill="none" stroke="#333" stroke-width="2.5"/></svg>Conceal Weapons Instructor</li>
  <li><svg width="16" height="16" viewBox="0 0 16 16"><rect x="1" y="3" width="12" height="12" fill="none" stroke="#333" stroke-width="1.5"/><path d="M4 8l3 3 8-10" fill="none" stroke="#333" stroke-width="2.5"/></svg>Law Enforcement Officer</li>
  <li><svg width="16" height="16" viewBox="0 0 16 16"><rect x="1" y="3" width="12" height="12" fill="none" stroke="#333" stroke-width="1.5"/><path d="M4 8l3 3 8-10" fill="none" stroke="#333" stroke-width="2.5"/></svg>CA DOJ Firearms Instructor</li>
  <li><svg width="16" height="16" viewBox="0 0 16 16"><rect x="1" y="3" width="12" height="12" fill="none" stroke="#333" stroke-width="1.5"/><path d="M4 8l3 3 8-10" fill="none" stroke="#333" stroke-width="2.5"/></svg>Law Enforcement Pistol &amp; Tactics Instructor</li>
</ul>

<h2 class="col-title" style="left:626px;top:1716px">Training <span>Videos</span></h2>
<div class="col-rule" style="left:626px;top:1772px;width:475px"><i></i></div>
<div class="video" role="img" aria-label="Video still of handcuffs and a guard badge on a table">
  <div class="video-title">California<br>Guard Card<br>License</div>
  <div class="play"><svg width="72" height="50" viewBox="0 0 72 50"><path d="M29 15l16 10-16 10z" fill="#fff"/></svg></div>
  <div class="video-bar">
    <svg width="473" height="34" viewBox="0 0 473 34"><rect x="14" y="11" width="4" height="12" fill="#fff"/><rect x="21" y="11" width="4" height="12" fill="#fff"/><rect x="40" y="16" width="300" height="3" fill="#666"/><rect x="40" y="16" width="150" height="3" fill="#cc1f1f"/><circle cx="190" cy="17.5" r="6" fill="#fff"/><rect x="366" y="12" width="14" height="10" fill="none" stroke="#fff" stroke-width="2"/><rect x="400" y="16" width="50" height="3" fill="#888"/><circle cx="430" cy="17.5" r="7" fill="#fff"/></svg>
  </div>
</div>

<section class="inquiry" role="img" aria-label="Soft golden photo backdrop of a support agent wearing a headset">
</section>
<div class="inquiry-pill"><div class="inner"><b>Make An Inquiry</b><span>Give Us A Call. (555) 014-2290</span></div></div>
<div class="inquiry-photo" role="img" aria-label="Round photo of a smiling call centre agent with a headset"></div>

<section class="social"></section>
<div class="feed" style="left:99px;border:3px solid var(--fb)">
  <div class="feed-head" style="background:var(--fb)"><span>Recent Activity</span><b>Circlebook</b></div>
  <div class="feed-item"><div class="thumb"></div><p style="color:var(--fb)">Lorem ipsum dolor sit amet the consectetuer adipi.<small>3 people recommended this.</small></p></div>
  <div class="feed-item"><div class="thumb"></div><p style="color:var(--fb)">Lorem ipsum dolor sit amet the adipiscing elit, sed di nonummy<small>3 people recommended this.</small></p></div>
  <div class="feed-item"><div class="thumb"></div><p style="color:var(--fb)">Lorem ipsum dolor sit amet the consectetuer adipiscing.<small>2 people recommended this.</small></p></div>
  <div class="feed-foot">Circlebook social plugin</div>
</div>
<div class="feed" style="left:396px;border:3px solid var(--tw)">
  <div class="feed-head" style="background:var(--tw)"><span>Latest Tweets</span><b>Chirpline</b></div>
  <div class="feed-item"><div class="avatar" role="img" aria-label="Profile photo"></div><p><b>Lorem <span style="color:#3a9ad9">@ipsumdolorsitamet</span></b><br>Lorem ipsum dolor sit amet.<small>7 minutes ago . Reply . Favorite</small></p></div>
  <div class="feed-item"><div class="avatar" role="img" aria-label="Profile photo"></div><p><b>Lorem <span style="color:#3a9ad9">@ipsumdolorsitamet</span></b><br>Lorem ipsum dolor sit amet.<small>27 minutes ago . Reply . Favorite</small></p></div>
  <div class="feed-item"><div class="avatar" role="img" aria-label="Profile photo"></div><p><b>Lorem <span style="color:#3a9ad9">@ipsumdolorsitamet</span></b><br>Lorem ipsum dolor sit amet.<small>58 minutes ago . Reply . Favorite</small></p></div>
  <div class="feed-foot" style="background:var(--tw);color:#fff">Join the conversation</div>
</div>
<div class="newsletter">
  <h4>Newsletter <span>Sign Up</span></h4>
  <p>Lorem ipsum dolor sit amet, consectetuer adipiscing elit, sed diam nonummy nibh euismod tincidunt ut laoreet dolore magna aliquam erat volutpat.</p>
  <small>(You may unsubscribe at anytime)</small>
  <div class="field"><svg width="12" height="12" viewBox="0 0 12 12"><circle cx="6" cy="3.5" r="3" fill="#aaa"/><path d="M0 12a6 5 0 0 1 12 0z" fill="#aaa"/></svg>Your Name</div>
  <div class="field"><svg width="13" height="10" viewBox="0 0 13 10"><rect width="13" height="10" fill="#aaa"/><path d="M0 0l6.5 5L13 0" fill="none" stroke="#fff"/></svg>Your email address</div>
  <div style="margin-top:14px"><span class="btn">Sign Up</span></div>
</div>

<footer class="site-footer">
  <h5 class="foot-title" style="left:99px">Quick <span>Links</span></h5>
  <ul class="foot-links">
    <li>Home</li><li>About Us</li><li>Our Services</li><li>Guardcarddesk</li><li>Security Jobs</li><li>Contact Us</li>
  </ul>
  <h5 class="foot-title" style="left:333px">Quick <span>Contact</span></h5>
  <div class="foot-input" style="top:80px">Enter your name</div>
  <div class="foot-input" style="top:126px">Enter your email</div>
  <div class="foot-input" style="top:172px;height:50px">Enter your message</div>
  <div class="btn" style="position:absolute;left:333px;top:234px;font-size:12px;padding:9px 24px">SUBMIT</div>
  <h5 class="foot-title" style="left:690px">Contact <span>Information</span></h5>
  <div class="foot-info">
    <b>Watchpost Learning Hub.</b><br>
    <span style="color:#aaa;font-size:11px">Lorem Ipsum' Will Uncover<br>Many - 123456 Lorem Ipsum</span>
    <div class="row" style="margin-top:10px"><svg width="12" height="16" viewBox="0 0 12 16"><rect x="1" y="0" width="10" height="16" rx="2" fill="#ddd"/><rect x="3" y="2" width="6" height="10" fill="#222"/></svg>(555) 014-2290</div>
    <div class="row"><svg width="14" height="14" viewBox="0 0 24 24"><path d="M5 2l5 5-3 3c1 3 4 6 7 7l3-3 5 5-3 4C10 23 1 14 1 5z" fill="#ddd"/></svg>(555) 014-2290</div>
    <div class="row"><svg width="14" height="14" viewBox="0 0 14 14"><rect x="3" y="0" width="8" height="4" fill="#ddd"/><rect x="0" y="4" width="14" height="7" fill="#ddd"/><rect x="3" y="9" width="8" height="5" fill="#ddd" stroke="#222"/></svg>(555) 014-2290</div>
  </div>
  <div class="foot-seal"></div>
</footer>
<div class="bottom-bar">
  <p>Copyright © 2016 Watchpost Learning Hub. | All Right Reserved</p>
  <div class="follow">Follow Us: <i></i><i></i><i></i><i></i><i></i><i></i></div>
</div>

</body>
</html>
```